Photo Storage Service - Web Application

This is web design for a simple photo storage service.
There is a web page and on the left side is a list of folders and on the right side there are photo thumbnails. By pressing a photo thumbnail, they will see the full size (it's just a link to a different page).
This project is limited only to ONE page, which is the page with the folders list and the thumbnails. However it contains some features that I will try to list here:
- Name of the service: Tavo Vault
- Location of account: http://username.tavo.example
- Folder list: Show all folders belonging to the user. Because you have to be able to drag photos to a folder, they have to be visible and cannot be hidden behind a menu item etc.
- Thumbnails with photos (in the future also videos)
- Adjusted view with smaller thumbnails and less space for folder list (so it is possible to view a larger quantity of thumbnails)- Select multiple thumbnails with rectangle- Show that a thumbnail is selected (maybe bold border?)
- Simple mobile view, but no emphasis on the mobile view in this design project.
- Drag one or more selected photos to a folder
- Delete one or more selected photos
- Drag a folder to another folder
- Rename folder
- Delete folder
- Create folder
- Show progress when deleting/moving (because it calls for every photo, so if there are 100 photos, it will delete 1 by 1 and it will take about 10 seconds - you could show progress bar or equivalent)
Background information: This is for a photo storage service NOT intended for sharing photos, but intended to indefinitely store photos and for yourself to browse your own photos.
It is a design requirement that it loads extremely fast. So we need to limit as much as possible extra graphics that cannot be done by CSS and other external libraries.
(I know this is ONLY design and nothing to do with CSS or libraries, but I can assess from the design if it might be heavy to load when implemented)
I have attached a crude screenshot of the current design, just for your understanding. It should not match this design and you are not in any way supposed to FIT your design into this same style or structure.
Target Market(s)
Consumers
Number of Pages Required
1 page
Font styles to use
Look and feel
Each slider illustrates characteristics of the customer's brand and the style your logo design should communicate.

```html
<!DOCTYPE html>
<html lang="en">
<head>
<meta charset="utf-8">
<title>Tavo Vault – My Photos</title>
<link href="https://fonts.googleapis.com/css2?family=Open+Sans:wght@400;600;700&display=swap" rel="stylesheet">
<style>
:root{
  --backdrop:#fde4ea;
  --surface:#ffffff;
  --band:#fff4f6;
  --brand:#ea2d5a;
  --brand-soft:#fde3ea;
  --ink:#2b2b2b;
  --muted:#8b8b8b;
  --line:#ececec;
  --field:#f4f4f4;
}
*{margin:0;padding:0;box-sizing:border-box}
html,body{width:1200px;height:1200px;overflow:hidden;background:var(--backdrop);font-family:"Open Sans",sans-serif;color:var(--ink)}
.app{position:absolute;left:62px;top:64px;width:1078px;height:1136px;background:var(--surface);overflow:hidden}
.brand{position:absolute;left:40px;top:16px;font-size:22px;font-weight:700;color:var(--brand);letter-spacing:-.3px}
.search{position:absolute;left:522px;top:19px;width:382px;height:24px;border-radius:12px;background:var(--field);font-size:8.5px;color:var(--muted);padding:6px 14px}
.search svg{position:absolute;right:10px;top:5px}
.submit{position:absolute;left:919px;top:18px;width:89px;height:25px;border:1px solid var(--line);border-radius:3px;font-size:8.5px;color:#555;display:flex;align-items:center;gap:5px;padding-left:10px}
.settings{position:absolute;left:1021px;top:22px}
.crumbs{position:absolute;left:0;top:61px;width:100%;height:24px;background:var(--band);border-bottom:1px solid #f7e3e8}
.crumbs .path{position:absolute;left:40px;top:6px;font-size:9px;color:var(--brand)}
.views{position:absolute;right:45px;top:5px;display:flex;gap:14px;font-size:9px;color:var(--brand)}
.views span{display:flex;align-items:center;gap:5px}
.folders{position:absolute;left:40px;top:108px;width:198px;height:654px;border:1px solid var(--line);box-shadow:0 1px 3px rgba(0,0,0,.05);list-style:none;padding-top:16px}
.folders li{height:24.9px;line-height:24.9px;font-size:10.5px;padding-left:25px}
.folders li.active{background:var(--brand-soft);color:var(--brand);font-weight:700;padding-left:36px;border-radius:0 13px 13px 0;width:187px}
.grid{position:absolute;left:258px;top:108px;display:grid;grid-template-columns:repeat(4,190.4px);grid-auto-rows:158.5px;gap:6.4px}
.grid a{display:block}
</style>
</head>
<body>
<div class="app">
  <div class="brand">Tavo Vault</div>
  <div class="search">Search image, category...
    <svg width="13" height="13" viewBox="0 0 13 13" fill="none" stroke="#999" stroke-width="1.2"><circle cx="5.5" cy="5.5" r="4.3"/><path d="M8.7 8.7l3.3 3.3"/></svg>
  </div>
  <div class="submit">
    <svg width="12" height="10" viewBox="0 0 12 10" fill="none" stroke="#666" stroke-width="1"><rect x=".5" y="2" width="11" height="7.5" rx="1"/><circle cx="6" cy="5.7" r="2"/><path d="M4 2l1-1.5h2L8 2"/></svg>
    Submit Photo
  </div>
  <svg class="settings" width="17" height="17" viewBox="0 0 20 20" fill="none" stroke="var(--brand)" stroke-width="1.4"><circle cx="10" cy="10" r="3"/><path d="M10 1.5l1.6 2.2 2.6-.8.5 2.7 2.6.9-.8 2.6 2 1.9-2 1.9.8 2.6-2.6.9-.5 2.7-2.6-.8L10 18.5l-1.6-2.2-2.6.8-.5-2.7-2.6-.9.8-2.6-2-1.9 2-1.9-.8-2.6 2.6-.9.5-2.7 2.6.8z"/></svg>
  <div class="crumbs">
    <span class="path">My Photos /</span>
    <div class="views">
      <span>Grid view <svg width="14" height="14" viewBox="0 0 14 14" fill="none" stroke="var(--brand)" stroke-width=".9" opacity=".6"><rect x=".5" y=".5" width="13" height="13"/><path d="M5 .5v13M9 .5v13M.5 5h13M.5 9h13"/></svg></span>
      <span>List view <svg width="14" height="14" viewBox="0 0 14 14" fill="none" stroke="var(--brand)" stroke-width=".9" opacity=".6"><rect x=".5" y=".5" width="13" height="13"/><path d="M.5 4.5h13M.5 7h13M.5 9.5h13"/></svg></span>
    </div>
  </div>
  <ul class="folders">
    <li>Inbox</li><li class="active">Favourite Photos</li><li>A day in Oslo</li><li>A your of Svendborg</li><li>Alicante 2017</li><li>Alicante after Christmas</li><li>Bandarban</li><li>Bird Lightly Garnished</li><li>Brazil</li><li>Days in Denmark - Christmas</li><li>Mobile Uploads</li><li>Random</li><li>Recently Uploaded from Phone</li><li>Sundarban</li><li>Sylhet II</li><li>Tea Garden</li><li>Thailand 1</li><li>Thailand 1</li><li>Thailand 2018</li><li>Timeline Photos</li><li>USA</li><li>UploadBag</li><li>Vancouver</li><li>Thumbnails</li><li>Videos/Thumbnails</li>
  </ul>
  <div class="grid">
    <a href="#" role="img" aria-label="Tall office towers seen from below" style="background:linear-gradient(100deg,#e8eaec,#7a6a5e 70%,#cfd2d5)"></a>
    <a href="#" role="img" aria-label="Man at a railing overlooking misty hills" style="background:linear-gradient(#e9e4dc,#8a8577 40%,#2f3438)"></a>
    <a href="#" role="img" aria-label="Blue leaves on dark background" style="background:radial-gradient(circle at 50% 50%,#1e5a78,#0b1a22)"></a>
    <a href="#" role="img" aria-label="Bride holding a bouquet under a veil" style="background:linear-gradient(90deg,#2e3430,#8a8f8a 60%,#c9c8c4)"></a>
    <a href="#" role="img" aria-label="Sunlit valley with cliffs and forest" style="background:linear-gradient(#d9c69a,#a89268 55%,#3d3a27)"></a>
    <a href="#" role="img" aria-label="Snowy city street with poster box and tram" style="background:linear-gradient(90deg,#8a2d2a,#a89c95 50%,#d5cfca)"></a>
    <a href="#" role="img" aria-label="Silhouette of a man at a window" style="background:radial-gradient(circle at 50% 40%,#3f7a94,#0d1a22)"></a>
    <a href="#" role="img" aria-label="Neon sign above a row of cushions" style="background:linear-gradient(#4a3a34,#3a2a26 70%,#6a3e34)"></a>
    <a href="#" role="img" aria-label="Hand holding a small flower at dusk" style="background:linear-gradient(#9a6a44,#3a2c26 60%,#1c1a1c)"></a>
    <a href="#" role="img" aria-label="Snowy slope under a starry sky" style="background:linear-gradient(#0c0e12 45%,#8f9296 70%,#d6d6d6)"></a>
    <a href="#" role="img" aria-label="City street with old buildings and wires" style="background:linear-gradient(#7fb3d8,#a78d7a 55%,#4a4540)"></a>
    <a href="#" role="img" aria-label="Misty blue mountain valley" style="background:linear-gradient(#eceff1,#6f8aa3 50%,#27394f)"></a>
    <a href="#" role="img" aria-label="Person in a yellow parking garage" style="background:linear-gradient(90deg,#c9b23a,#4f4b3e 50%,#c9b23a)"></a>
    <a href="#" role="img" aria-label="Drink cup on a wooden table" style="background:linear-gradient(#d7d7d4 35%,#b48656 55%,#8b6238)"></a>
    <a href="#" role="img" aria-label="Spiral staircase from above" style="background:radial-gradient(circle at 45% 45%,#333,#9a9c9e 40%,#e4e5e6)"></a>
    <a href="#" role="img" aria-label="Colourful abstract paint swirl" style="background:linear-gradient(135deg,#c93a1f,#2f9a3b 35%,#e8d23a 60%,#2b5ea8)"></a>
    <a href="#" role="img" aria-label="Icy waterfall in blue light" style="background:linear-gradient(#2a4f8a,#a9c2e2 55%,#e7eef7)"></a>
    <a href="#" role="img" aria-label="Red wall with painted lettering" style="background:#ef5663"></a>
    <a href="#" role="img" aria-label="Laptop and breakfast on a desk from above" style="background:linear-gradient(#8a8078,#5a524c 50%,#a89a8c)"></a>
    <a href="#" role="img" aria-label="Surfer riding a turquoise wave" style="background:linear-gradient(#8fb5d2,#e8edf0 45%,#2d8a8f 70%,#12424a)"></a>
    <a href="#" role="img" aria-label="Bride holding a bouquet under a veil" style="background:linear-gradient(90deg,#c9c8c4,#8a8f8a 50%,#2e3430)"></a>
    <a href="#" role="img" aria-label="Blue leaves on dark background" style="background:radial-gradient(circle at 50% 50%,#1e5a78,#0b1a22)"></a>
    <a href="#" role="img" aria-label="Man at a railing overlooking misty hills" style="background:linear-gradient(#e9e4dc,#8a8577 40%,#2f3438)"></a>
    <a href="#" role="img" aria-label="Tall office towers seen from below" style="background:linear-gradient(260deg,#e8eaec,#7a6a5e 70%,#cfd2d5)"></a>
    <a href="#" role="img" aria-label="Neon sign above a row of cushions" style="background:linear-gradient(#4a3a34,#3a2a26)"></a>
    <a href="#" role="img" aria-label="Silhouette of a man at a window" style="background:linear-gradient(#2f6c88,#0d1a22)"></a>
    <a href="#" role="img" aria-label="Snowy city street with poster box and tram" style="background:linear-gradient(90deg,#d5cfca,#a89c95 50%,#8a2d2a)"></a>
    <a href="#" role="img" aria-label="Sunlit valley with cliffs and forest" style="background:linear-gradient(#e3d5b2,#a89268)"></a>
  </div>
</div>
</body>
</html>
```